Korvane Sky Works, LLC - Business Card

I currently have a drone business that specializes in aerial photography, thermal image inspections, deer recovery, search and rescue, custom agricultural applications. i will attach my current business card as well as some logos to incorporate for a new up to date business card
Updates

Designs look the same

Sick

Target Market(s)

farmers, hunters

Contact Information for Business Card

name address phone number (as existing card i attached)

Requirements
Must have
• im good with existing business card, but would like an agricultural twist

```html
<!DOCTYPE html>
<html lang="en">
<head>
<meta charset="utf-8">
<title>Korvane Sky Works, LLC – Business Card</title>
<link href="https://fonts.googleapis.com/css2?family=Archivo:wght@500;700;800&family=Inter:wght@400;500&display=swap" rel="stylesheet">
<style>
  :root {
    --backdrop: #d3d4d6;
    --card: #ffffff;
    --ink: #111111;
    --green: #3f8b3a;
    --green-light: #5ea94a;
    --field-light: #e9e4dc;
    --field-mid: #d6cfc2;
    --sky-soft: #dfe6ea;
  }
  * { box-sizing: border-box; margin: 0; padding: 0; }
  html, body { width: 900px; height: 1200px; overflow: hidden; }
  body {
    background: var(--backdrop);
    font-family: "Inter", Arial, sans-serif;
    color: var(--ink);
    position: relative;
  }
  .card {
    position: absolute;
    left: 134px;
    width: 632px;
    height: 364px;
    background: var(--card);
    overflow: hidden;
  }
  .card--front { top: 210px; }
  .card--back { top: 624px; }

  .aerial-photo {
    position: absolute; inset: 0;
    background:
      radial-gradient(ellipse 28% 14% at 22% 50%, var(--sky-soft), transparent 70%),
      radial-gradient(ellipse 22% 14% at 86% 56%, var(--sky-soft), transparent 70%),
      linear-gradient(170deg, #e2d6c8 0%, var(--field-light) 35%, #e3e3d9 65%, var(--field-mid) 100%);
  }
  .front-brand {
    position: absolute;
    left: 0; right: 0; top: 150px;
    text-align: center;
    font-family: "Archivo", Arial, sans-serif;
    font-weight: 800;
    font-size: 54px;
    letter-spacing: 2px;
    color: var(--green);
  }

  .back-brand {
    position: absolute;
    left: 40px; top: 64px;
    font-family: "Archivo", Arial, sans-serif;
    font-weight: 800;
    font-size: 28px;
    letter-spacing: 1px;
    color: var(--green);
  }
  .person { position: absolute; left: 358px; top: 58px; }
  .person__name {
    font-family: "Archivo", Arial, sans-serif;
    font-weight: 700;
    font-size: 25px;
    letter-spacing: 0.5px;
    line-height: 1;
  }
  .person__role {
    margin-top: 4px;
    font-family: "Archivo", Arial, sans-serif;
    font-weight: 500;
    font-size: 14px;
    color: var(--green-light);
  }

  .services, .contacts { position: absolute; list-style: none; }
  .services { left: 40px; top: 162px; }
  .services li {
    display: flex; align-items: center;
    height: 31px;
    font-size: 14.5px;
    letter-spacing: -0.2px;
  }
  .services svg { width: 24px; height: 10px; margin-right: 6px; }
  .contacts { left: 358px; top: 198px; }
  .contacts li {
    display: flex; align-items: center;
    height: 29px;
    font-size: 14.5px;
    letter-spacing: -0.1px;
  }
  .contacts svg { width: 15px; height: 15px; margin-right: 6px; fill: var(--green); }

  .footer-bars { position: absolute; left: 40px; top: 323px; }
</style>
</head>
<body>

<section class="card card--front">
  <div class="aerial-photo" role="img" aria-label="Soft aerial photograph of farmland with a barn, ponds and bare trees"></div>
  <div class="front-brand">Korvane</div>
</section>

<section class="card card--back">
  <div class="back-brand">Korvane</div>

  <div class="person">
    <div class="person__name">DALEN MORROW</div>
    <div class="person__role">Owner</div>
  </div>

  <ul class="services">
    <li><svg viewBox="0 0 24 10"><path d="M1 3h22M4 3v2h16V3" stroke="#3f8b3a" stroke-width="1.6" fill="none"/><circle cx="12" cy="6" r="2.5" fill="none" stroke="#3f8b3a" stroke-width="1.4"/></svg>Thermal Image Inspections</li>
    <li><svg viewBox="0 0 24 10"><path d="M1 3h22M4 3v2h16V3" stroke="#3f8b3a" stroke-width="1.6" fill="none"/><circle cx="12" cy="6" r="2.5" fill="none" stroke="#3f8b3a" stroke-width="1.4"/></svg>Deer Recovery</li>
    <li><svg viewBox="0 0 24 10"><path d="M1 3h22M4 3v2h16V3" stroke="#3f8b3a" stroke-width="1.6" fill="none"/><circle cx="12" cy="6" r="2.5" fill="none" stroke="#3f8b3a" stroke-width="1.4"/></svg>Search &amp; Rescue</li>
    <li><svg viewBox="0 0 24 10"><path d="M1 3h22M4 3v2h16V3" stroke="#3f8b3a" stroke-width="1.6" fill="none"/><circle cx="12" cy="6" r="2.5" fill="none" stroke="#3f8b3a" stroke-width="1.4"/></svg>Real Estate Photography</li>
    <li><svg viewBox="0 0 24 10"><path d="M1 3h22M4 3v2h16V3" stroke="#3f8b3a" stroke-width="1.6" fill="none"/><circle cx="12" cy="6" r="2.5" fill="none" stroke="#3f8b3a" stroke-width="1.4"/></svg>Custom Agricultural Applications</li>
  </ul>

  <ul class="contacts">
    <li><svg viewBox="0 0 24 24"><path d="M6.6 10.8a15 15 0 0 0 6.6 6.6l2.2-2.2c.3-.3.7-.4 1-.2 1.1.4 2.3.6 3.6.6.6 0 1 .4 1 1V20c0 .6-.4 1-1 1A17 17 0 0 1 3 4c0-.6.4-1 1-1h3.5c.6 0 1 .4 1 1 0 1.3.2 2.5.6 3.6.1.3 0 .7-.2 1z"/></svg>555-018-2264</li>
    <li><svg viewBox="0 0 24 24"><path d="M2 5h20v14H2z M2 5l10 8 10-8" fill="#3f8b3a" stroke="#fff" stroke-width="1.2"/></svg>hello@korvaneskyworks.com</li>
    <li><svg viewBox="0 0 24 24"><circle cx="12" cy="12" r="9" fill="none" stroke="#3f8b3a" stroke-width="2"/><path d="M3 12h18M12 3c3 3 3 15 0 18M12 3c-3 3-3 15 0 18" fill="none" stroke="#3f8b3a" stroke-width="1.6"/></svg>www.korvaneskyworks.com</li>
    <li><svg viewBox="0 0 24 24"><path d="M12 2a7 7 0 0 0-7 7c0 5 7 13 7 13s7-8 7-13a7 7 0 0 0-7-7zm0 9.5a2.5 2.5 0 1 1 0-5 2.5 2.5 0 0 1 0 5z"/></svg>214 W. Orchard Rd. Alder, OH 45000</li>
  </ul>

  <svg class="footer-bars" width="554" height="20" viewBox="0 0 554 20">
    <polygon points="0,0 288,0 268,20 0,20" fill="#111111"/>
    <polygon points="297,0 554,0 554,20 277,20" fill="#3f8b3a"/>
  </svg>
</section>

</body>
</html>
```